Online Rug Store needs Clearance Banner

Website is: Lanternfield Carpets and Home
You can access it at: www.lanternfieldcarpetsandhome.com and login (top right) with password: trazok

*** update: When creating banners for my site, you have permission to use images from www.velbora.com, but ONLY for this project. The images/artwork are copyright allowable for use on www.lanternfieldcarpetsandhome.com projects.***

We need a home page banner sized 1000 wide x 500 tall pixels to promote a "Clearance Sale" on rugs. The banner can state:

1. Clearance Sale
2. Now in progress
3. Save an extra 20% with coupon code 'Mint20'
4. Ends March 31st
5. Plus Free Shipping and 30 day returns.

We prefer a banner that appears hand-drawn and artistic, not commercially produced. It is OK to use a room scene image, rug images, or just a colored/textured background with text and no images. Your choice.

Flat graphics with no shadows and 3-D effect preferred.
Attached is are 3 logo options, as well as an example banner with handcrafted, artistic styling that we prefer.

Target Market(s)

This should be an eye-catching banner to showcase a very urgent promotion. Consider using colors of red, white, gold, and black to make a strong statement on the home page.

Industry/Entity Type

Home And Garden

Requirements
Must have
• Winner must provide Photoshop editable file format (.psd format) including layers that can be edited.
Nice to have
• Hand-drawn, stenciled, scribbled, artistic graphics and fonts is nice because we sell rugs that are made by hand.
Should not have
• little to no shadowing. Avoid computerized graphics.

```html
<!DOCTYPE html>
<html lang="en">
<head>
<meta charset="utf-8">
<title>Lanternfield Carpets and Home — Clearance Sale</title>
<link rel="stylesheet" href="https://fonts.googleapis.com/css2?family=Bebas+Neue&family=Cinzel:wght@400;700&family=Oswald:wght@600&family=Arimo:wght@700&display=swap">
<style>
  :root {
    --paper: #ffffff;
    --ink: #0b0b0b;
    --maroon: #7a1414;
    --rust: #b6401c;
    --sand: #c9bba3;
    --olive: #9aa55a;
    --slate: #6f90ad;
    --cream: #e7dfcf;
    --gold: #b89a55;
  }
  html, body { margin: 0; padding: 0; overflow: hidden; }
  body { width: 1200px; height: 637px; background: var(--paper); }
  .banner { position: relative; width: 1200px; height: 637px; background: var(--paper); overflow: hidden; }
  .pennants { position: absolute; inset: 0; }
  .status {
    position: absolute; left: 783px; top: 174px; margin: 0; white-space: nowrap;
    font-family: "Cinzel", serif; font-size: 36px; color: var(--maroon); letter-spacing: 1.5px;
  }
  .brand-box {
    position: absolute; left: 68px; top: 270px; width: 337px; height: 99px;
    background: var(--ink); display: flex; align-items: center; justify-content: center; gap: 12px;
  }
  .brand-mark { width: 22px; height: 22px; background: var(--maroon); flex: none; }
  .brand-name {
    font-family: "Cinzel", serif; color: var(--paper); font-size: 19px; line-height: 1.15; margin: 0;
  }
  .headline {
    position: absolute; left: 432px; top: 258px; margin: 0; white-space: nowrap;
    font-family: "Bebas Neue", sans-serif; font-weight: 400; font-size: 146px; line-height: 1;
    color: var(--ink); letter-spacing: 0;
    transform: scaleX(0.86); transform-origin: left top;
  }
  .deadline {
    position: absolute; left: 937px; top: 305px; width: 190px; height: 23px; box-sizing: border-box;
    background: var(--maroon); color: var(--paper); text-align: center; line-height: 23px;
    font-family: "Cinzel", serif; font-weight: 700; font-size: 16px; letter-spacing: .3px; white-space: nowrap;
  }
  .offer {
    position: absolute; left: 432px; top: 376px; margin: 0; white-space: nowrap;
    font-family: "Oswald", sans-serif; font-weight: 600; font-size: 33px; color: var(--maroon);
    letter-spacing: .4px; text-transform: uppercase;
  }
  .perks {
    position: absolute; left: 432px; top: 428px; margin: 0;
    font-family: "Arimo", sans-serif; font-weight: 700; font-size: 19px; line-height: 1.2;
    color: var(--ink); text-transform: uppercase;
  }
</style>
</head>
<body>
<main class="banner">
  <svg class="pennants" width="1200" height="637" viewBox="0 0 1200 637">
    <g role="img" aria-label="Row of triangular rug swatch pennants in sand, rust and olive stripes">
      <polygon points="36,36 284,36 210,210" fill="var(--sand)"/>
      <polygon points="152,36 390,36 318,210" fill="var(--rust)"/>
      <polygon points="282,36 612,36 436,210" fill="var(--olive)"/>
    </g>
    <polygon role="img" aria-label="Small maroon and gold rug swatch pennant" points="944,36 1126,36 1035,126" fill="var(--maroon)"/>
    <polygon role="img" aria-label="Small maroon and gold rug swatch pennant" points="70,600 250,600 160,510" fill="var(--maroon)"/>
    <g role="img" aria-label="Row of rug swatch pennants pointing up in slate blue, cream damask and gold floral">
      <polygon points="590,600 815,600 716,440" fill="var(--slate)"/>
      <polygon points="718,600 960,600 838,436" fill="var(--cream)"/>
      <polygon points="840,600 1160,600 978,436" fill="var(--gold)"/>
    </g>
  </svg>

  <p class="status">NOW IN PROGRESS</p>

  <div class="brand-box">
    <span class="brand-mark"></span>
    <p class="brand-name">Lanternfield<br>Carpets and Home</p>
  </div>

  <h1 class="headline">CLEARANCE SALE</h1>
  <span class="deadline">ENDS MARCH 31ST</span>
  <p class="offer">Save an extra 20% with coupon code 'Mint20'</p>
  <p class="perks">Plus free shipping and<br>30 day returns.</p>
</main>
</body>
</html>
```